New Flyer Design Project

I need to make a flyer with the dishes I make
With a fixed price zone, phone number 0648352917, Facebook: Tia Marilse Filipino Food

Target Market(s)

Customers of open-air markets, individuals, and special orders

Industry/Entity Type

Food truck

Font styles to use
Decorative
Script

```html
<!DOCTYPE html>
<html lang="en">
<head>
<meta charset="utf-8">
<title>Filipino Street Food Flyer</title>
<link href="https://fonts.googleapis.com/css2?family=Lobster&family=Roboto+Condensed:wght@400;700&display=swap" rel="stylesheet">
<style>
:root{
  --red:#d8182e;
  --crimson:#8c0f2a;
  --navy:#0e1f5c;
  --blue:#1c3fa8;
  --ink:#1a1a2e;
  --white:#ffffff;
  --cream:#fff3e0;
  --badge:#ffffff;
  --badge-text:#1a1a2e;
  --outline:#3a0a14;
}
*{margin:0;padding:0;box-sizing:border-box}
html,body{width:1200px;height:2256px;overflow:hidden}
body{font-family:"Roboto Condensed",Arial,sans-serif;background:#7a7a7a}
.flyer{
  position:relative;width:1200px;height:2256px;overflow:hidden;
  background:
    radial-gradient(ellipse 60% 18% at 50% 10%, rgba(255,255,255,.98) 0%, rgba(255,255,255,.85) 40%, rgba(255,255,255,0) 100%),
    radial-gradient(ellipse 70% 50% at 0% 30%, var(--red) 0%, rgba(216,24,46,0) 70%),
    radial-gradient(ellipse 70% 55% at 100% 35%, var(--blue) 0%, rgba(28,63,168,0) 70%),
    linear-gradient(160deg, var(--crimson) 0%, #5a1a4f 45%, var(--navy) 75%, #060b24 100%);
}
.header{position:absolute;top:60px;left:0;width:100%;text-align:center}
.header .kicker{
  font-weight:700;letter-spacing:10px;color:var(--blue);font-size:46px;
  position:absolute;left:250px;top:18px;
}
.header .title{
  font-family:"Lobster",cursive;font-weight:400;font-size:220px;line-height:1;color:var(--red);
  -webkit-text-stroke:3px var(--outline);margin-top:60px;
}
.menu{
  position:absolute;top:450px;left:75px;width:1050px;
  display:grid;grid-template-columns:repeat(4,240px);column-gap:30px;row-gap:36px;
}
.dish{height:350px}
.dish .photo{position:relative;width:240px;height:260px;border:3px solid var(--white);box-shadow:0 4px 12px rgba(0,0,0,.4)}
.dish .price{
  position:absolute;top:-14px;right:-14px;width:60px;height:60px;border-radius:50%;
  background:var(--badge);color:var(--badge-text);font-weight:700;font-size:22px;
  display:flex;align-items:center;justify-content:center;box-shadow:0 2px 6px rgba(0,0,0,.4)
}
.dish .name{color:var(--white);font-weight:700;font-size:22px;line-height:1.15;margin-top:12px}
.dish .desc{color:var(--cream);font-size:16px;margin-top:4px;opacity:.85}
.p1{background:linear-gradient(135deg,#c98a3a,#6b3a12)}
.p2{background:linear-gradient(135deg,#b3402a,#4a1b10)}
.p3{background:linear-gradient(135deg,#d9cfc0,#8a7a66)}
.p4{background:linear-gradient(135deg,#9c5a2a,#3d2010)}
.p5{background:linear-gradient(135deg,#e0b050,#8a5a20)}
.p6{background:linear-gradient(135deg,#6a8a3a,#2c3a18)}
.p7{background:linear-gradient(135deg,#a8602a,#4d2a12)}
.p8{background:linear-gradient(135deg,#d8a040,#7a4a18)}
.p9{background:linear-gradient(135deg,#f0d060,#b08020)}
.footer{position:absolute;left:75px;top:2030px;width:1050px;height:170px;display:flex;align-items:center;color:var(--white)}
.brand{display:flex;align-items:center;gap:12px;width:260px;font-weight:700;font-size:24px}
.brand .dot{width:56px;height:56px;border-radius:50%;background:var(--red);flex:none}
.contacts{flex:1;font-size:30px;font-weight:700;padding-left:20px}
.contacts .row{display:flex;align-items:center;gap:14px;margin:8px 0}
.contacts .row.small{font-size:24px;font-weight:400}
.contacts .sq{width:28px;height:28px;background:var(--blue);border-radius:4px;flex:none}
.divider{width:3px;height:130px;background:var(--white);margin:0 30px}
.avail{font-size:34px;line-height:1.2;width:260px}
</style>
</head>
<body>
<main class="flyer">
  <header class="header">
    <div class="kicker">FILIPINO</div>
    <h1 class="title">Street Food</h1>
  </header>

  <section class="menu">
    <article class="dish"><div class="photo p1" role="img" aria-label="Photo of lumpia spring rolls"><span class="price">€8</span></div><p class="name">Filipino Rice Bowl with Lumpia And Adobo</p><p class="desc">Ingredients and Description</p></article>
    <article class="dish"><div class="photo p2" role="img" aria-label="Photo of chicken adobo bowl"><span class="price">€8</span></div><p class="name">Filipino Rice Bowl with Lumpia And Adobo</p><p class="desc">Ingredients and Description</p></article>
    <article class="dish"><div class="photo p3" role="img" aria-label="Photo of steamed buns"><span class="price">€8</span></div><p class="name">Filipino Rice Bowl with Lumpia And Adobo</p><p class="desc">Ingredients and Description</p></article>
    <article class="dish"><div class="photo p4" role="img" aria-label="Photo of grilled skewers"><span class="price">€8</span></div><p class="name">Filipino Rice Bowl with Lumpia And Adobo</p><p class="desc">Ingredients and Description</p></article>

    <article class="dish"><div class="photo p4" role="img" aria-label="Photo of pork dish"><span class="price">€8</span></div><p class="name">Filipino Rice Bowl with Lumpia And Adobo</p><p class="desc">Ingredients and Description</p></article>
    <article class="dish"><div class="photo p3" role="img" aria-label="Photo of rice bowl"><span class="price">€8</span></div><p class="name">Filipino Rice Bowl with Lumpia And Adobo</p><p class="desc">Ingredients and Description</p></article>
    <article class="dish"><div class="photo p7" role="img" aria-label="Photo of braised meat"><span class="price">€8</span></div><p class="name">Filipino Rice Bowl with Lumpia And Adobo</p><p class="desc">Ingredients and Description</p></article>
    <article class="dish"><div class="photo p8" role="img" aria-label="Photo of banana rolls"><span class="price">€8</span></div><p class="name">Filipino Rice Bowl with Lumpia And Adobo</p><p class="desc">Ingredients and Description</p></article>

    <article class="dish"><div class="photo p9" role="img" aria-label="Photo of leche flan dessert"><span class="price">€8</span></div><p class="name">Filipino Rice Bowl with Lumpia And Adobo</p><p class="desc">Ingredients and Description</p></article>
    <article class="dish"><div class="photo p6" role="img" aria-label="Photo of noodle dish"><span class="price">€8</span></div><p class="name">Filipino Rice Bowl with Lumpia And Adobo</p><p class="desc">Ingredients and Description</p></article>
    <article class="dish"><div class="photo p2" role="img" aria-label="Photo of stir-fried meat"><span class="price">€8</span></div><p class="name">Filipino Rice Bowl with Lumpia And Adobo</p><p class="desc">Ingredients and Description</p></article>
    <article class="dish"><div class="photo p1" role="img" aria-label="Photo of fried rolls"><span class="price">€8</span></div><p class="name">Filipino Rice Bowl with Lumpia And Adobo</p><p class="desc">Ingredients and Description</p></article>

    <article class="dish"><div class="photo p5" role="img" aria-label="Photo of fried snacks"><span class="price">€8</span></div><p class="name">Filipino Rice Bowl with Lumpia And Adobo</p><p class="desc">Ingredients and Description</p></article>
    <article class="dish"><div class="photo p7" role="img" aria-label="Photo of savoury dish"><span class="price">€8</span></div><p class="name">Filipino Rice Bowl with Lumpia And Adobo</p><p class="desc">Ingredients and Description</p></article>
    <article class="dish"><div class="photo p8" role="img" aria-label="Photo of sweet dessert"><span class="price">€3</span></div><p class="name">Filipino Rice Bowl with Lumpia And Adobo</p><p class="desc">Ingredients and Description</p></article>
  </section>

  <footer class="footer">
    <div class="brand"><span class="dot"></span><span>Tia Marilse</span></div>
    <div class="contacts">
      <div class="row">
        <svg width="28" height="28" viewBox="0 0 24 24" aria-hidden="true"><path fill="#ffffff" d="M6.6 10.8a15 15 0 0 0 6.6 6.6l2.2-2.2a1 1 0 0 1 1-.25 11.4 11.4 0 0 0 3.6.57 1 1 0 0 1 1 1V20a1 1 0 0 1-1 1A17 17 0 0 1 3 4a1 1 0 0 1 1-1h3.5a1 1 0 0 1 1 1c0 1.25.2 2.450.57 3.57a1 1 0 0 1-.25 1z"/></svg>
        <span>0648352917</span>
      </div>
      <div class="row small"><span class="sq"></span><span>Tia Marilse Filipino Food</span></div>
    </div>
    <div class="divider"></div>
    <div class="avail">Available at<br>Open-Air Markets</div>
  </footer>
</main>
</body>
</html>
```